Cafe menu design

Hi there,

We need a editable menu layout and design to match our new cafe call: " Harlow Bean Roasters", we love the ideas of A4 clip board and self print out menu in black and white. ( Example as attached)

We would like the menu can be break down into category easy for customer to flip around and read. ( example as attached)

Category including the following:

- All day breakfast and Sandwich and Toast
- Main (Lunch&Dinner) and Pizza
- Dessert snacks and nibbles
- Hot and Cold Drinks
- Catering menu

Please find our logo and our current menu as attached for your information and convenience.
Updates

Dear Designers, Thank you for your time and submission, Please find our drink menu and logo as attached. Kind Regards,

Target Market(s)

Young family, young Couple, office and corporate staff

Industry/Entity Type

Cafe

Font styles to use
Serif
Sans Serif

```html
<!DOCTYPE html>
<html lang="en">
<head>
<meta charset="utf-8">
<title>Main Menu – Harlow Bean Roasters</title>
<link rel="stylesheet" href="https://fonts.googleapis.com/css2?family=Special+Elite&family=Courier+Prime:wght@400;700&display=swap">
<style>
  :root {
    --paper: #ffffff;
    --ink: #231f20;
    --rule: #3a3a3a;
  }
  html, body {
    margin: 0;
    padding: 0;
    width: 939px;
    height: 1200px;
    overflow: hidden;
    background: var(--paper);
  }
  .menu-page {
    position: relative;
    width: 939px;
    height: 1200px;
    background: var(--paper);
    color: var(--ink);
    font-family: "Courier Prime", "Courier New", monospace;
    box-sizing: border-box;
    border: 1px solid var(--rule);
  }
  .page-frame {
    position: absolute;
    left: 0;
    top: 0;
  }
  .page-title {
    position: absolute;
    left: 100px;
    top: 82px;
    margin: 0;
    font-family: "Special Elite", "Courier New", monospace;
    font-weight: 400;
    font-size: 132px;
    line-height: 1;
    letter-spacing: 2px;
    color: var(--ink);
  }
  .title-bar {
    position: absolute;
    left: 463px;
    top: 222px;
    width: 74px;
    height: 11px;
    background: var(--ink);
  }
  .entry, .section-label, .entry-note {
    position: absolute;
    left: 103px;
    width: 701px;
    top: var(--y);
    font-size: 15px;
    line-height: 19px;
    margin: 0;
  }
  .section-label {
    text-decoration: underline;
    text-underline-offset: 3px;
    text-transform: uppercase;
  }
  .entry {
    display: flex;
    justify-content: space-between;
    border-bottom: 1px solid var(--rule);
    height: 18px;
  }
  .entry.no-rule { border-bottom: none; }
  .entry-price { text-align: right; }
  .brand-name {
    position: absolute;
    left: 0;
    width: 939px;
    top: 1082px;
    text-align: center;
    font-size: 24px;
    line-height: 28px;
    font-weight: 700;
    letter-spacing: 2px;
    color: var(--ink);
  }
</style>
</head>
<body>
<main class="menu-page">
  <svg class="page-frame" width="939" height="1200" viewBox="0 0 939 1200" aria-hidden="true">
    <path d="M76 38 H857 A44 44 0 0 0 901 82 V1117 A44 44 0 0 0 857 1161 H76 A44 44 0 0 0 32 1117 V82 A44 44 0 0 0 76 38 Z"
          fill="none" stroke="var(--ink)" stroke-width="2.5"/>
  </svg>

  <h1 class="page-title">main</h1>
  <span class="title-bar"></span>

  <h2 class="section-label" style="--y:290px">Meat</h2>
  <p class="entry" style="--y:321px"><span>Gourmet Panini</span><span class="entry-price">10</span></p>
  <p class="entry-note" style="--y:340px">- Spanish pulled pork &amp; braised onion</p>
  <p class="entry-note" style="--y:359px">- Flame grilled meatball &amp; cranberry sauce</p>
  <p class="entry-note" style="--y:387px">Extras:</p>
  <p class="entry" style="--y:408px"><span>Beer battered chips</span><span class="entry-price">4</span></p>
  <p class="entry" style="--y:428px"><span>Side salad</span><span class="entry-price">4</span></p>
  <p class="entry" style="--y:459px"><span>Aussie barbeque beef ribs</span><span class="entry-price">18</span></p>
  <p class="entry-note" style="--y:478px">with special sauce,beer battered chips &amp; green leaf salad</p>
  <p class="entry" style="--y:509px"><span>Stack Aussie beef burger</span><span class="entry-price">16</span></p>
  <p class="entry-note" style="--y:528px">With bacon rasher, beetroot, cheese, tomato, green leaf salad</p>
  <p class="entry-note" style="--y:548px">&amp; beer battered chips</p>
  <p class="entry" style="--y:578px"><span>Chicken schnitzel, parmesan burger</span><span class="entry-price">14</span></p>
  <p class="entry-note" style="--y:598px">with beer battered chips, cheese , tomato &amp; green leaf salad</p>

  <h2 class="section-label" style="--y:649px">Seafood</h2>
  <p class="entry" style="--y:678px"><span>Grilled Tasmania salmon fillet</span><span class="entry-price">18</span></p>
  <p class="entry-note" style="--y:699px">with char grilled zucchini salad</p>
  <p class="entry" style="--y:728px"><span>Classic fish &amp; chips</span><span class="entry-price">15</span></p>
  <p class="entry-note" style="--y:748px">2 Battered barramundi fillets, tartar sauce, chips &amp; salad</p>
  <p class="entry no-rule" style="--y:779px"><span>Barramundi fish burger</span><span class="entry-price">15</span></p>
  <p class="entry-note" style="--y:798px">Swiss cheese, tartar sauce,tomato with chips &amp; green leaf salad</p>

  <h2 class="section-label" style="--y:841px">Vegetarian</h2>
  <p class="entry" style="--y:871px"><span>Grilled haloumi &amp; green olives</span><span class="entry-price">10</span></p>
  <p class="entry" style="--y:902px"><span>Vegetarian burger</span><span class="entry-price">15</span></p>
  <p class="entry-note" style="--y:922px">Grilled haloumi, char-grilled eggplants, red capsicum, pesto &amp; salad</p>

  <h2 class="section-label" style="--y:964px">Kids</h2>
  <p class="entry" style="--y:995px"><span>Kids Fish &amp; Chips</span><span class="entry-price">7.5</span></p>
  <p class="entry" style="--y:1025px"><span>Kids Chicken &amp; Chips</span><span class="entry-price">7.5</span></p>
  <p class="entry" style="--y:1056px"><span>Wholemeal sourdough with Nocciola chocolate spread</span><span class="entry-price">4</span></p>

  <div class="brand-name">HARLOW BEAN ROASTERS</div>
</main>
</body>
</html>
```